High End Cosmetic Packaging Design Project

Looking for packaging for 2 products for a High end skin care line aimed at the 35+ year old women. Color scheme is Pantone 2765c with accents of metallic silver, copper or gold, Pantone colors 871-877c. Possible watermark in the background or a 3D image. We are open to any good ideas and suggestions. Box dimensions for the 2 products are small, approximately 4.375 inches high and 1.5 inches square. I have attached an image of the logo. I have the logo files in all the various forms. 1 box is for a Vitamin C Serum and the other box is for an Anti Aging Serum. Boxes are the same but the text will be different on both products. I will supply the text for the boxes later, including directions & ingredients and a UPC code that has to go on the underside of the box. It has to be an elegant design that will stand out in photos online. Good and quick communication & feedback between you and us is essential. I have attached a jpg of our new logo. I have this logo in all available forms
*****We are open to all ideas and want your ideas and input. The bottles that go inside these boxes are a deep violet almost black velkar glass. This is where the pantone color selection came from but upon further thought it may not be the right choice. We were out looking at cosmetic packaging today and thought also as an idea that a dark charcoal, or black box might work as well. We have seen boxes in those dark shades in glossy, matt and some with a sparkle finish. Embossed lettering may be a possibility as well. Copper letters may be an idea that works well also. These are just ideas rolling aroung in our heads but please give us your ideas*******
This is for the 35+ year old woman.
Communication

```html
<!DOCTYPE html>
<html lang="en">
<head>
<meta charset="utf-8">
<title>Lumeva Labs – Vitamin C Serum Carton Dieline</title>
<link href="https://fonts.googleapis.com/css2?family=Exo+2:wght@300;400;500&display=swap" rel="stylesheet">
<style>
  :root {
    --paper: #ffffff;
    --carton: #231f20;
    --ink: #e6efeb;
    --bottle-glow: #2f2b2c;
  }
  * { margin: 0; padding: 0; box-sizing: border-box; }
  html, body { width: 1200px; height: 1000px; overflow: hidden; background: var(--paper); }
  .canvas { position: relative; width: 1200px; height: 1000px; font-family: "Exo 2", sans-serif; color: var(--ink); }
  .dieline { position: absolute; inset: 0; }
  .panel { position: absolute; text-align: center; }

  /* lined sub-brand */
  .lined { display: flex; align-items: center; justify-content: center; gap: 8px; }
  .lined::before, .lined::after { content: ""; display: block; height: 1px; background: var(--ink); }

  /* top tuck flap (printed upside down) */
  .top-flap { left: 258px; top: 118px; width: 190px; height: 120px; transform: rotate(180deg); }
  .top-flap .flap-brand { position: absolute; top: 0; left: 0; width: 100%; font-size: 42px; font-weight: 300; letter-spacing: 2px; line-height: 1; }
  .top-flap .flap-sub { position: absolute; top: 48px; left: 0; width: 100%; font-size: 11px; font-weight: 300; letter-spacing: 8px; }
  .top-flap .flap-sub::before, .top-flap .flap-sub::after { width: 40px; }
  .top-flap .flap-product { position: absolute; top: 84px; left: 0; width: 100%; font-size: 19px; font-weight: 400; letter-spacing: 0.5px; }

  /* ingredients side panel */
  .ingredients { left: 262px; top: 308px; width: 180px; font-size: 9.4px; line-height: 1.27; }
  .ingredients h3 { font-size: 11.5px; font-weight: 500; }
  .maker { left: 262px; top: 616px; width: 180px; font-size: 9.4px; line-height: 1.27; }

  /* front panel */
  .bottle-art { position: absolute; left: 486px; top: 296px; width: 116px; height: 346px;
    background: linear-gradient(180deg, var(--bottle-glow), var(--carton)); border-radius: 10px 10px 18px 18px; }
  .front-title { left: 515px; top: 534px; text-align: left; font-size: 17.5px; font-weight: 400; line-height: 1.16; }
  .front-tag { left: 448px; top: 656px; width: 190px; font-size: 14px; font-weight: 500; letter-spacing: 0.6px; }

  /* brand panel */
  .brand-name { position: absolute; left: 0; top: 0; }
  .brand-name text { font-family: "Exo 2", sans-serif; font-weight: 300; font-size: 92px; fill: var(--ink); }
  .brand-sub { left: 640px; top: 619px; width: 190px; font-size: 20px; font-weight: 300; letter-spacing: 6px; }
  .brand-sub::before, .brand-sub::after { width: 34px; }
  .product-name { left: 620px; top: 648px; width: 230px; font-size: 18.5px; font-weight: 500; }
  .volume { left: 620px; top: 675px; width: 230px; font-size: 10px; }

  /* directions panel */
  .directions { left: 832px; top: 310px; width: 184px; font-size: 9.4px; line-height: 1.27; }
  .directions h3 { font-size: 11.5px; font-weight: 500; }
  .directions .gap { margin-top: 14px; }
</style>
</head>
<body>
<div class="canvas">
  <svg class="dieline" width="1200" height="1000" viewBox="0 0 1200 1000" aria-hidden="true">
    <polygon fill="var(--carton)" points="283,55 423,55 448,85 448,280 1018,280 1018,692 608,692 608,888 583,913 473,913 448,888 448,692 258,692 228,662 228,310 258,280 258,85"/>
  </svg>

  <div class="panel top-flap">
    <div class="flap-brand">LUMEVA</div>
    <div class="flap-sub lined">LABS</div>
    <div class="flap-product">Vitamin C Serum</div>
  </div>

  <div class="panel ingredients">
    <h3>Ingredients</h3>
    <p>Organic Herbal Infusion, Organic Aloe Barbadensis Leaf (Aloe), Sodium Ascorbyl Phosphate (Vitamin C), Methylsulfonylmethane (MSM), Cassia Angustifolia Seed Polysaccharide (botanical hyaluronic acid), Hamamelis Virginiana (Witch Hazel), Kosher Vegetable Glycerin, Carbomer, (2s)-2-Amino-5-guanidinopentanoic Acid, Kosher Vegetable Glycerin, Organic Rosa Canina (Rosehip Seed Oil), Organic Sesamum Indicum (Sesame) Seed Oil, Silk Protein Amino Acid Blend (Sodium L-Pyrrolidone Carboxylate, Sodium Lactate, L-Arginine, L-Aspartic Acid, L-Pyrrolidonecarboxylic Acid, Glycine, L-Alanine, L-Serine, L-Valine, L-Proline, L-threonine, L-Isoleucine, L-Histidine, L-Phenylalanine), Organic Helianthus Annuus (Sunflower Oil), Organic Simmondsia Chinensis (Jojoba Oil), Phenoxyethanol, Ethyl Hexyl Glycerin.</p>
  </div>
  <div class="panel maker">
    <p>Manufactured For<br>Lumeva Labs<br>48 Alder Grove Ct, Suite B12<br>Fairview GA 30411</p>
  </div>

  <div class="bottle-art" role="img" aria-label="Line drawing of a dropper serum bottle"></div>
  <div class="panel front-title">Advanced<br>Vitamin C<br>Serum</div>
  <div class="panel front-tag">BIOPHOTONIC</div>

  <svg class="brand-name" width="1200" height="1000" viewBox="0 0 1200 1000" aria-label="Lumeva">
    <text transform="translate(700,296) rotate(90)" x="0" y="0" textLength="322" lengthAdjust="spacingAndGlyphs">LUMEVA</text>
  </svg>
  <div class="panel brand-sub lined">LABS</div>
  <div class="panel product-name">Vitamin C Serum</div>
  <div class="panel volume">1oz/30ml</div>

  <div class="panel directions">
    <h3>Directions for use</h3>
    <p>Use in the morning and additionally at bed time if necessary. Wash and pat dry your skin. Apply a small amount to your face, neck, under eyes and areas needed allowing the serum to fully absorb. May be used under a moisturizer or under makeup.</p>
    <p class="gap">For External Use Only</p>
    <p class="gap">An Advanced 18% Concentrate<br>In Pure Hyaluronic Acid<br>Super Antioxidant<br>Helps Fade Sun Spots<br>Protects &amp; Hydrates Skin</p>
    <p class="gap">Biophotonic Glass Is Scientifically Proven To Retain &amp; Improve The Freshness &amp; Potency Of The Product.</p>
  </div>
</div>
</body>
</html>
```